Designs for a Barrister's chambers

Design stationery (including business card and letterhead) for a barrister's chambers -- similar to a law firm, using the enclosed logo. The current designs are not fit for purpose.

```html
<!DOCTYPE html>
<html lang="en">
<head>
<meta charset="utf-8">
<title>Ledgerfield Chambers – Business Card</title>
<link rel="stylesheet" href="https://fonts.googleapis.com/css2?family=Nunito+Sans:wght@400;600;700;800&display=swap">
<style>
  :root {
    --bg: #c4c4c4;
    --paper: #ffffff;
    --navy: #16202e;
    --navy-deep: #0f1722;
    --teal: #1e9fbf;
    --rule: #35c3ea;
    --ink: #1c2533;
    --muted: #3a4352;
  }
  * { margin: 0; padding: 0; box-sizing: border-box; }
  html, body {
    width: 1200px; height: 876px; overflow: hidden;
    background: var(--bg);
    font-family: "Nunito Sans", Arial, sans-serif;
  }
  .stage {
    width: 1200px; height: 876px;
    display: flex; align-items: center; justify-content: center; gap: 60px;
  }
  .card {
    position: relative;
    width: 525px; height: 300px;
    border-radius: 3px;
    box-shadow: 0 10px 28px rgba(0,0,0,.22);
    overflow: hidden;
  }
  /* Front */
  .card--front { background: var(--paper); color: var(--ink); }
  .holder { position: absolute; left: 34px; top: 34px; }
  .holder__name { font-size: 24px; font-weight: 800; color: var(--navy); letter-spacing: -.2px; line-height: 1.15; }
  .holder__role { font-size: 17px; font-weight: 400; color: var(--teal); margin-top: 2px; }
  .divider {
    position: absolute; left: 34px; right: 34px; top: 122px;
    height: 2px; background: var(--rule);
  }
  .contacts { position: absolute; left: 34px; top: 142px; list-style: none; }
  .contacts li {
    display: flex; align-items: flex-start; gap: 8px;
    font-size: 12.5px; line-height: 16px; color: var(--muted);
    margin-bottom: 6px;
  }
  .icon {
    flex: none; width: 15px; height: 15px; border-radius: 3px;
    background: var(--teal); display: flex; align-items: center; justify-content: center;
    margin-top: 1px;
  }
  .address {
    position: absolute; right: 34px; top: 142px;
    display: flex; align-items: flex-end; gap: 8px;
    font-size: 13px; line-height: 17px; color: var(--ink); text-align: right;
  }
  .wordmark {
    display: flex; align-items: center; gap: 10px;
    font-weight: 800; color: var(--navy); line-height: 1.02;
  }
  .wordmark__square { background: var(--teal); flex: none; }
  .card--front .wordmark { position: absolute; right: 34px; top: 40px; font-size: 23px; }
  .card--front .wordmark__square { width: 30px; height: 30px; }
  /* Back */
  .card--back {
    background: linear-gradient(155deg, #1d2836 0%, var(--navy) 45%, var(--navy-deep) 100%);
    display: flex; align-items: center; justify-content: center;
  }
  .card--back .wordmark { color: #ffffff; font-size: 34px; gap: 14px; }
  .card--back .wordmark__square { width: 42px; height: 42px; }
</style>
</head>
<body>
<main class="stage">
  <section class="card card--front" aria-label="Business card front">
    <div class="holder">
      <h1 class="holder__name">Martin Calloway</h1>
      <p class="holder__role">Barrister</p>
    </div>
    <div class="wordmark"><span class="wordmark__square"></span><span>Ledgerfield<br>Chambers</span></div>
    <div class="divider"></div>
    <ul class="contacts">
      <li>
        <span class="icon"><svg width="9" height="9" viewBox="0 0 10 10"><path d="M2 1h2l1 2.5-1.3.8a5 5 0 0 0 2 2L6.5 5 9 6v2a1 1 0 0 1-1 1A7 7 0 0 1 1 2a1 1 0 0 1 1-1z" fill="#fff"/></svg></span>
        <span>0203 555 0148<br>07700 900 321</span>
      </li>
      <li>
        <span class="icon"><svg width="9" height="9" viewBox="0 0 10 10"><rect x="1" y="2" width="8" height="6" fill="none" stroke="#fff" stroke-width="1.2"/><path d="M1 2l4 3.5L9 2" fill="none" stroke="#fff" stroke-width="1.2"/></svg></span>
        <span>martin.calloway@ledgerfieldchambers.com</span>
      </li>
      <li>
        <span class="icon"><svg width="9" height="9" viewBox="0 0 10 10"><circle cx="5" cy="5" r="3.8" fill="none" stroke="#fff" stroke-width="1.1"/><path d="M1.2 5h7.6M5 1.2c-2 2.5-2 5.1 0 7.6M5 1.2c2 2.5 2 5.1 0 7.6" fill="none" stroke="#fff" stroke-width=".9"/></svg></span>
        <span>www.ledgerfieldchambers.com</span>
      </li>
    </ul>
    <div class="address">
      <span>42 Temple Row, London<br>EC4Y 7AA</span>
      <span class="icon"><svg width="9" height="9" viewBox="0 0 10 10"><path d="M5 9.5S1.8 6 1.8 3.9a3.2 3.2 0 0 1 6.4 0C8.2 6 5 9.5 5 9.5z" fill="#fff"/><circle cx="5" cy="3.9" r="1.2" fill="#1e9fbf"/></svg></span>
    </div>
  </section>

  <section class="card card--back" aria-label="Business card back">
    <div class="wordmark"><span class="wordmark__square"></span><span>Ledgerfield<br>Chambers</span></div>
  </section>
</main>
</body>
</html>
```